Brill Insurance Agency - Business Cards

Hello, I am needing new trendy business cards for our Insurance Agency now that I have a new Logo. I have attached our new logo with several color options along with a business card design that I like. I am leaning towards burgundy and blue colors. I have attached our current business card. I have also attached a headshot of our company president, Martin Vale, that you can use if you wish. Thank you so much in advance for all the wonderful designs!!!!

Target Market(s)

We want to look very professional to potential customers and we also want to look very professional so insurance companies will want to contract with us to sell their product.

Industry/Entity Type

Insurance

Contact Information for Business Card

Martin Vale
mvale@brillagency.com
Business: 555-213-4087
Fax: 555-213-7751
Cell: 555-390-2618
Toll Free: 888-555-0194
42 W Elm Rd Larkston, MO 64999
www.brillagency.net

Font styles to use
Serif
Sans Serif

Colors
0355a3
3277b5
f04a50
ec1f27

Requirements
Nice to have
• I love creativity. The more creative and balanced a business card design the more I will like it. I would like the card to be printed horizontally instead of vertically.
Should not have
• My project should not have the Allied Coverage Network logo. It is no longer used in the industry.

```html
<!DOCTYPE html>
<html lang="en">
<head>
<meta charset="utf-8">
<title>Brill Insurance Agency – Business Cards</title>
<link href="https://fonts.googleapis.com/css2?family=Roboto:wght@400;500;700&display=swap" rel="stylesheet">
<style>
  :root {
    --navy: #212a5e;
    --grey: #4a4a4c;
    --white: #ffffff;
    --backdrop: #d3e6ec;
  }
  html, body {
    margin: 0;
    width: 1200px;
    height: 900px;
    overflow: hidden;
    background: var(--backdrop);
    font-family: "Roboto", Arial, sans-serif;
  }
  .card {
    position: absolute;
    left: 250px;
    width: 700px;
    height: 400px;
    border-radius: 22px;
    overflow: hidden;
    box-shadow: 0 6px 18px rgba(20, 40, 60, 0.25);
  }
  .card-front { top: 40px; background: var(--navy); color: var(--white); }
  .card-back { top: 460px; background: var(--white); }

  .wordmark {
    position: absolute;
    display: flex;
    align-items: center;
    gap: 18px;
  }
  .wordmark-dot {
    border-radius: 50%;
    border: 6px solid currentColor;
    box-sizing: border-box;
  }
  .wordmark-text {
    font-weight: 700;
    text-transform: uppercase;
    line-height: 1.15;
  }
  .card-front .wordmark { left: 120px; top: 140px; }
  .card-front .wordmark-dot { width: 96px; height: 96px; }
  .card-front .wordmark-divider { width: 2px; height: 120px; background: var(--white); }
  .card-front .wordmark-text { font-size: 34px; letter-spacing: 1px; }
  .card-front .wordmark-text span { display: block; font-size: 20px; letter-spacing: 7px; }

  .front-web {
    position: absolute;
    left: 0; right: 0; bottom: 40px;
    text-align: center;
    font-size: 17px;
  }

  .card-back .wordmark { left: 36px; top: 64px; color: var(--navy); gap: 12px; }
  .card-back .wordmark-dot { width: 52px; height: 52px; border-width: 5px; }
  .card-back .wordmark-text { font-size: 24px; }
  .card-back .wordmark-text span { display: block; font-size: 14px; letter-spacing: 5px; }

  .wave { position: absolute; inset: 0; }

  .holder {
    position: absolute;
    right: 40px; top: 30px;
    text-align: right;
    color: var(--navy);
  }
  .holder-name { font-size: 24px; font-weight: 700; margin: 0; }
  .holder-role { font-size: 12px; color: var(--grey); margin: 2px 0 0; }

  .contacts {
    position: absolute;
    right: 36px; top: 168px;
    margin: 0; padding: 0;
    list-style: none;
    color: var(--white);
    font-size: 15px;
  }
  .contacts li {
    display: flex;
    justify-content: flex-end;
    align-items: center;
    gap: 12px;
    height: 25px;
  }
  .contacts svg { width: 15px; height: 15px; fill: var(--white); }

  .address {
    position: absolute;
    left: 150px; bottom: 28px;
    color: var(--white);
    font-size: 16px;
    line-height: 1.35;
    text-align: center;
  }
</style>
</head>
<body>

<section class="card card-front">
  <div class="wordmark">
    <div class="wordmark-dot"></div>
    <div class="wordmark-divider"></div>
    <div class="wordmark-text">Brill Insurance<span>Agency Inc</span></div>
  </div>
  <div class="front-web">www.brillagency.net</div>
</section>

<section class="card card-back">
  <svg class="wave" viewBox="0 0 700 400" preserveAspectRatio="none">
    <path fill="#4a4a4c" d="M0,272 C160,262 250,272 330,210 C420,142 500,105 700,82 L700,400 L0,400Z"/>
    <path fill="#ffffff" d="M0,300 C150,292 240,300 335,232 C430,162 510,126 700,112 L700,400 L0,400Z"/>
    <path fill="#212a5e" d="M0,308 C150,300 245,306 340,240 C435,170 515,134 700,120 L700,400 L0,400Z"/>
  </svg>

  <div class="wordmark">
    <div class="wordmark-dot"></div>
    <div class="wordmark-text">Brill Insurance<span>Agency Inc</span></div>
  </div>

  <div class="holder">
    <p class="holder-name">Martin Vale</p>
    <p class="holder-role">President</p>
  </div>

  <ul class="contacts">
    <li>555-213-4087 (Business)
      <svg viewBox="0 0 16 16"><path d="M3 1l3 3-1.5 2a9 9 0 0 0 5.5 5.5L12 10l3 3-2 2C7 15 1 9 1 3z"/></svg></li>
    <li>888-555-0194 (Toll Free)
      <svg viewBox="0 0 16 16"><path d="M4 0h8v16H4zM5.5 2v10h5V2z"/></svg></li>
    <li>555-390-2618
      <svg viewBox="0 0 16 16"><path d="M1 6c0-3 14-3 14 0v2h-4V6H5v2H1zM3 9h10v6H3z"/></svg></li>
    <li>555-213-7751
      <svg viewBox="0 0 16 16"><path d="M4 1h7v4H4zM2 6h12v9H2z"/></svg></li>
    <li>mvale@brillagency.com
      <svg viewBox="0 0 16 16"><path d="M1 3h14L8 9zM1 5l7 5 7-5v8H1z"/></svg></li>
  </ul>

  <div class="address">42 W Elm Rd Larkston, MO 64999<br>www.brillagency.net</div>
</section>

</body>
</html>
```